Corporate Profile, with ALOT more work for winning bidder

We need
1. CD designed
2. CD Cover Designed
3. 2x Envelope's designed
4. Letter head designed
The designer picked will also get many further projects from us. Almost totaling 10k a year.
- More info
• Software installation disc
a. Logo
b. Contact details (See below)
c. Instructions
o “Please insert CD into computer and follow the prompts”
d. Title
o “Free Software Installation Disc”
• CD Sleave double sided
- Front
o Logo
o Website Address
o Facebook address
o Title
? “Free Software Installation Disc”
• Letter head
- Logo
- Contact information
- A4 paper size
• C4 Envelope
- Nicely Designed with logo
- A window to put address
- Printed return address (See below) on back
• DL Envelope, to return to us
- Had our return address ( See below)
- Nice design
Contact details
Machines Near You
7b Fenwick Crescent Bayswater, Vic, 3153
www.MachinesNearYou.example.au
1300 42 65 19
www.Facebook.com/MachinesNearYou
Return Address
Machines Near You
7b Fenwick Crescent
Larkfield, Tas, 7321

```html
<!DOCTYPE html>
<html lang="en">
<head>
<meta charset="utf-8">
<title>Machines Near You – Stationery</title>
<link href="https://fonts.googleapis.com/css2?family=Arimo:wght@400;700&display=swap" rel="stylesheet">
<style>
  :root {
    --stage: #000000;
    --paper: #ffffff;
    --brand-blue: #3aa6dd;
    --brand-blue-deep: #2b97d1;
    --art-light: #d6ecf9;
    --art-mid: #5db8e6;
    --ink: #1d2a33;
    --ink-soft: #4a5860;
    --rule: #c9d3d8;
  }
  * { box-sizing: border-box; margin: 0; padding: 0; }
  html, body { width: 900px; height: 1200px; overflow: hidden; background: var(--stage); }
  body { position: relative; font-family: "Arimo", Arial, sans-serif; color: var(--ink); }

  .sheet { position: absolute; background: var(--paper); overflow: hidden; }

  .brand { position: absolute; display: flex; align-items: center; gap: 6px; z-index: 2; }
  .brand-mark { background: var(--brand-blue); flex: none; }
  .brand-name { font-weight: 700; color: var(--ink); letter-spacing: 0.02em; white-space: nowrap; }

  .contact { position: absolute; line-height: 1.5; color: var(--ink-soft); white-space: nowrap; font-style: normal; z-index: 2; }
  .contact-block { border-left: 1px solid var(--rule); padding-left: 6px; }
  .contact-line { display: flex; align-items: center; gap: 4px; }
  .contact-icon { width: 1.1em; height: 1.1em; flex: none; }

  .footer-band {
    position: absolute; left: 0; right: 0; bottom: 0; z-index: 3;
    background: var(--brand-blue);
    color: var(--paper); font-weight: 700;
    display: flex; align-items: center; justify-content: flex-end;
  }

  .hands-art {
    position: absolute; z-index: 1;
    border-radius: 18px;
    background: radial-gradient(ellipse at 50% 50%, var(--art-light) 0 45%, var(--art-mid) 70%, var(--brand-blue-deep) 100%);
  }

  /* Letterhead */
  .letterhead { left: 40px; top: 72px; width: 396px; height: 558px; }
  .letterhead .brand { left: 22px; top: 30px; }
  .letterhead .brand-mark { width: 18px; height: 18px; }
  .letterhead .brand-name { font-size: 10px; }
  .letterhead .contact { left: 250px; top: 22px; font-size: 6.5px; }
  .letterhead .footer-band { height: 12px; font-size: 6px; padding-right: 14px; }
  .letterhead .hands-art { right: -6px; bottom: 10px; width: 110px; height: 76px; }

  /* DL envelope front */
  .dl-front { left: 454px; top: 148px; width: 416px; height: 206px; }
  .dl-front .brand { left: 18px; top: 36px; }
  .dl-front .brand-mark { width: 14px; height: 14px; }
  .dl-front .brand-name { font-size: 8px; }
  .dl-front .footer-band { height: 12px; font-size: 6px; padding-right: 28px; }
  .dl-front .hands-art { right: -6px; bottom: 12px; width: 96px; height: 82px; }

  /* DL envelope back */
  .dl-back { left: 454px; top: 368px; width: 416px; height: 204px; }
  .dl-back .flap { position: absolute; inset: 0; }
  .dl-back .brand { left: 176px; top: 38px; }
  .dl-back .brand-mark { width: 10px; height: 10px; }
  .dl-back .brand-name { font-size: 6px; }
  .dl-back .contact { left: 46px; top: 150px; font-size: 6px; }

  /* C4 envelope */
  .c4-front { left: 120px; top: 660px; width: 610px; height: 434px; }
  .c4-front .brand { left: 28px; top: 36px; }
  .c4-front .brand-mark { width: 26px; height: 26px; }
  .c4-front .brand-name { font-size: 13px; }
  .c4-front .contact { left: 36px; top: 340px; font-size: 8.5px; }
  .c4-front .footer-band { height: 18px; font-size: 8px; padding-right: 28px; }
  .c4-front .hands-art { right: -8px; bottom: 20px; width: 200px; height: 142px; }
</style>
</head>
<body>

  <section class="sheet letterhead" aria-label="Letterhead">
    <div class="brand"><span class="brand-mark"></span><span class="brand-name">MACHINES NEAR YOU</span></div>
    <address class="contact contact-block">
      <div>Machines Near You</div>
      <div>7b Fenwick Crescent Larkfield, Tas, 7321</div>
      <div class="contact-line">
        <svg class="contact-icon" viewBox="0 0 10 10"><rect width="10" height="10" rx="2" fill="var(--brand-blue)"/><path d="M3 2.5c0 2.5 2 4.5 4.5 4.5l.5-1-1.5-.7-.6.6c-.8-.4-1.4-1-1.8-1.8l.6-.6L4 2z" fill="#fff"/></svg>
        <span>1300 42 65 19</span>
      </div>
      <div class="contact-line">
        <svg class="contact-icon" viewBox="0 0 10 10"><rect width="10" height="10" rx="2" fill="var(--brand-blue)"/></svg>
        <span>MachinesNearYou</span>
      </div>
    </address>
    <div class="hands-art" role="img" aria-label="Illustration of hands holding a blank screen"></div>
    <div class="footer-band">www.MachinesNearYou.example.au</div>
  </section>

  <section class="sheet dl-front" aria-label="DL envelope front">
    <div class="brand"><span class="brand-mark"></span><span class="brand-name">MACHINES NEAR YOU</span></div>
    <div class="hands-art" role="img" aria-label="Illustration of hands holding a blank screen"></div>
    <div class="footer-band">www.MachinesNearYou.example.au</div>
  </section>

  <section class="sheet dl-back" aria-label="DL envelope back">
    <svg class="flap" viewBox="0 0 416 204" preserveAspectRatio="none" aria-hidden="true">
      <polygon points="0,0 416,0 416,14 258,70 158,70 0,14" fill="var(--brand-blue)"/>
      <line x1="4" y1="22" x2="32" y2="204" stroke="var(--rule)" stroke-width="1"/>
      <line x1="412" y1="22" x2="384" y2="204" stroke="var(--rule)" stroke-width="1"/>
    </svg>
    <div class="brand"><span class="brand-mark"></span><span class="brand-name">MACHINES NEAR YOU</span></div>
    <address class="contact contact-block">
      <div>Machines Near You</div>
      <div>7b Fenwick Crescent Larkfield, Tas, 7321</div>
      <div class="contact-line">
        <svg class="contact-icon" viewBox="0 0 10 10"><rect width="10" height="10" rx="2" fill="var(--brand-blue)"/><path d="M3 2.5c0 2.5 2 4.5 4.5 4.5l.5-1-1.5-.7-.6.6c-.8-.4-1.4-1-1.8-1.8l.6-.6L4 2z" fill="#fff"/></svg>
        <span>1300 42 65 19</span>
      </div>
      <div class="contact-line">
        <svg class="contact-icon" viewBox="0 0 10 10"><rect width="10" height="10" rx="2" fill="var(--brand-blue)"/></svg>
        <span>MachinesNearYou</span>
      </div>
    </address>
  </section>

  <section class="sheet c4-front" aria-label="C4 envelope front">
    <div class="brand"><span class="brand-mark"></span><span class="brand-name">MACHINES NEAR YOU</span></div>
    <address class="contact contact-block">
      <div>Machines Near You</div>
      <div>7b Fenwick Crescent Larkfield, Tas, 7321</div>
      <div class="contact-line">
        <svg class="contact-icon" viewBox="0 0 10 10"><rect width="10" height="10" rx="2" fill="var(--brand-blue)"/><path d="M3 2.5c0 2.5 2 4.5 4.5 4.5l.5-1-1.5-.7-.6.6c-.8-.4-1.4-1-1.8-1.8l.6-.6L4 2z" fill="#fff"/></svg>
        <span>1300 42 65 19</span>
      </div>
      <div class="contact-line">
        <svg class="contact-icon" viewBox="0 0 10 10"><rect width="10" height="10" rx="2" fill="var(--brand-blue)"/></svg>
        <span>MachinesNearYou</span>
      </div>
    </address>
    <div class="hands-art" role="img" aria-label="Illustration of hands holding a blank screen"></div>
    <div class="footer-band">www.MachinesNearYou.example.au</div>
  </section>

</body>
</html>
```